Modern Website Design for PollMeridian – CX & Loyalty SaaS Platform

We need a modern, professional, and responsive website design for our B2B SaaS platform, PollMeridian. We help companies collect real-time customer feedback, analyze insights, and improve loyalty — combining a powerful CX platform with expert consulting services. The website should clearly communicate who we are and what we offer within the first impression. It should balance data-driven visuals such as dashboards, analytics, and charts with a human, approachable feel. The design must include at least six key pages: Homepage, Product/Services, About, Blog/Resources, Contact/Demo, and Pricing. It should be conversion-focused with clear calls-to-action that encourage visitors to request a demo or contact us. The site must be fully responsive across desktop, tablet, and mobile. It should support multiple languages, starting with English and Danish. Most importantly, the delivery must be a final WordPress website, ready to go live, not just design files.

Target Market(s)

Our target market is medium-to-large B2B organizations. The primary audience includes CX leaders, executives, and managers in customer success and service who want to measure loyalty, understand customer insights, and improve retention.

Industry/Entity Type

Technology / SaaS / Customer Experience

Coding

Coded - Design and coding required

Number of Pages Required

5+ page

Font styles to use
Sans Serif

Requirements
Must have
• The project must deliver a final WordPress website that is fully responsive across all devices. The design should be clean, modern, and SaaS-inspired, with clear calls-to-action on every page. It must also support English and Danish, with a visible language toggle. The site should include visuals of dashboards and analytics that reflect data-driven insights. It must feature sections for case studies or testimonials to build trust. The copywriting should be SEO-friendly, and the design should include smooth animations or hover effects that add polish without making the website feel heavy.
Should not have
• Cluttered layouts, or generic stock photos such as handshakes

```html
<!DOCTYPE html>
<html lang="en">
<head>
<meta charset="utf-8">
<title>PollMeridian – CX &amp; Loyalty Platform</title>
<link href="https://fonts.googleapis.com/css2?family=Roboto:ital,wght@0,400;0,500;0,700;0,900;1,400;1,700&display=swap" rel="stylesheet">
<style>
:root{
  --orange:#f04e12;
  --orange-dark:#e03d0a;
  --blue:#2a5aa8;
  --blue-dark:#1f4c97;
  --navy:#1c1a4f;
  --ink:#2a2a3a;
  --muted:#8a8d98;
  --line:#d9dce4;
  --bg-soft:#eef0f4;
  --white:#fff;
}
*{box-sizing:border-box;margin:0;padding:0}
html,body{width:1200px;height:3718px;overflow:hidden}
body{font-family:'Roboto',sans-serif;color:var(--ink);background:var(--white);position:relative}
.abs{position:absolute}
a{color:inherit;text-decoration:none}

/* header */
.brand{left:144px;top:116px;display:flex;align-items:center;gap:12px}
.brand-mark{width:34px;height:34px;background:var(--orange)}
.brand-name{font-size:38px;font-weight:700;color:var(--navy);letter-spacing:-.5px}
.call{left:786px;top:30px;display:flex;align-items:center;gap:14px}
.diamond-ico{width:34px;height:34px;transform:rotate(45deg);border-radius:4px;display:flex;align-items:center;justify-content:center}
.diamond-ico svg{transform:rotate(-45deg)}
.call-text{font-size:16px;line-height:22px;color:var(--navy);font-weight:500}
.call-text b{color:var(--blue);font-weight:500;display:block}
.nav{left:480px;top:96px;font-size:14px;font-weight:500;color:var(--navy)}
.nav a{position:absolute;white-space:nowrap}
.nav a.active::after{content:"";position:absolute;left:0;right:0;bottom:-7px;height:2px;background:var(--orange)}
.lang{left:995px;top:96px;display:flex;align-items:center;gap:6px;font-size:13px;font-weight:500;color:var(--navy)}
.flag{width:16px;height:16px;border-radius:50%;background:var(--blue-dark);border:2px solid #d33}

/* decorative accent areas */
.accent{border-radius:28px}
.accent-hero{left:812px;top:182px;width:368px;height:540px;background:linear-gradient(160deg,var(--orange) 0%,#f47a3f 45%,var(--blue) 100%);opacity:.92}
.accent-who{left:0;top:1668px;width:420px;height:560px;background:linear-gradient(150deg,var(--orange) 0%,#d9552a 40%,var(--blue) 100%);border-radius:0 28px 28px 0}

/* hero */
.hero-title{left:144px;top:282px;font-size:39px;line-height:59px;color:var(--navy);font-weight:400}
.hero-title strong{font-weight:700}
.hero-sub{left:144px;top:472px;font-size:19px;line-height:31px;color:#5b5e6b}
.btn{display:flex;align-items:center;justify-content:center;gap:12px;font-size:14px;font-weight:700;border-radius:8px;text-transform:uppercase}
.btn-primary{background:var(--orange);color:var(--white)}
.btn-outline{border:2px solid var(--blue);color:var(--blue);background:var(--white)}
.dots{left:572px;top:749px;display:flex;gap:9px}
.dots i{width:6px;height:6px;transform:rotate(45deg);background:var(--orange);display:block}
.dots i.on{background:var(--blue)}

/* section titles */
.sec-title{left:0;width:1200px;text-align:center;font-size:47px;color:var(--navy);font-weight:400}
.sec-title strong{font-weight:900}

/* offer */
.offer-text{text-align:center;width:240px}
.offer-text h3{font-size:20px;font-weight:700;color:var(--navy);margin-bottom:12px;white-space:nowrap}
.offer-text p{font-size:15.5px;line-height:25px;color:var(--muted)}
.offer-text.feature{width:270px}
.offer-text.feature h3{color:var(--white);font-size:22px}
.offer-text.feature p{color:var(--white);font-size:17px;line-height:28px}

/* who */
.who-title{left:623px;top:1742px;font-size:47px;color:var(--white);font-weight:400}
.who-title strong{font-weight:900}
.who-copy{left:623px;top:1819px;width:426px;font-size:15.6px;line-height:28.8px;color:var(--white);text-align:justify}

/* cases */
.case{background:var(--white);border:2px solid var(--line);padding:22px 22px}
.case.lift{box-shadow:0 6px 18px rgba(0,0,0,.12);border-color:#e6e7ec}
.case-head{display:flex;gap:14px}
.date{flex:none;width:44px;height:46px;color:var(--white);text-align:center;font-weight:700;line-height:1}
.date b{display:block;font-size:21px;padding-top:5px}
.date span{font-size:14px;font-weight:500}
.case h4{font-size:17px;line-height:22px;color:var(--navy);font-weight:500}
.case p{font-size:14px;line-height:21px;color:var(--muted);margin-top:12px}
.case .more{display:block;margin-top:6px;font-size:13px;font-weight:700;color:var(--orange)}

/* reviews */
.rev-title{left:0;width:1200px;top:2939px;text-align:center;font-size:47px;color:var(--white);font-weight:400}
.rev-title strong{font-weight:900}
.rev-quote{left:200px;width:800px;top:3022px;text-align:center;font-size:18px;line-height:32px;color:var(--white);font-style:italic}
.rev-name{left:0;width:1200px;top:3134px;display:flex;justify-content:center;align-items:center;gap:12px;font-size:20px;font-weight:700;font-style:italic;color:var(--white)}

/* footer */
.f-brand{left:0;width:1200px;top:3380px;display:flex;justify-content:center;align-items:center;gap:12px}
.f-contact{display:flex;align-items:center;gap:16px;font-size:14px;line-height:20px;color:#3a3a48}
.f-nav{left:0;width:1200px;top:3556px;display:flex;justify-content:center;gap:46px;font-size:16px;font-weight:500;color:var(--navy)}
.copy{left:0;width:1200px;top:3608px;text-align:center;font-size:14px;color:#3a3a48}
.social{left:551px;top:3660px;display:flex;gap:7px}
.social i{width:28px;height:28px;border-radius:50%;display:block}
</style>
</head>
<body>

<!-- header -->
<div class="abs brand"><span class="brand-mark"></span><span class="brand-name">PollMeridian</span></div>

<div class="abs call">
  <div class="diamond-ico" style="background:var(--orange)">
    <svg width="14" height="14" viewBox="0 0 24 24"><path fill="#fff" d="M6.6 10.8c1.4 2.8 3.8 5.2 6.6 6.6l2.2-2.2c.3-.3.7-.4 1-.2 1.1.4 2.3.6 3.6.6.6 0 1 .4 1 1V20c0 .6-.4 1-1 1C10.6 21 3 13.4 3 4c0-.6.4-1 1-1h3.5c.6 0 1 .4 1 1 0 1.3.2 2.5.6 3.6.1.3 0 .7-.2 1z"/></svg>
  </div>
  <div class="call-text"><b>Call Us</b>+1 555 014 2090</div>
</div>

<nav class="abs nav">
  <a class="active" style="left:0">HOME</a>
  <a style="left:74px">PRODUCTS</a>
  <a style="left:181px">ABOUT</a>
  <a style="left:260px">BLOG</a>
  <a style="left:328px">CONTACT</a>
  <a style="left:427px">PRICING</a>
</nav>
<div class="abs lang"><span class="flag"></span>EN
  <svg width="10" height="6" viewBox="0 0 10 6"><path d="M0 0h10L5 6z" fill="var(--navy)"/></svg>
</div>

<!-- hero -->
<div class="abs accent accent-hero" role="img" aria-label="Decorative orange and blue geometric accent"></div>
<svg class="abs" style="left:0;top:0" width="1200" height="830" viewBox="0 0 1200 830">
  <path d="M0 760 Q600 840 1200 760" fill="none" stroke="#e6e8ee" stroke-width="3"/>
</svg>

<h1 class="abs hero-title"><strong>COLLECT REAL-TIME</strong><br>CUSTOMER FEEDBACK<br><strong>&amp; IMPROVE LOYALTY</strong></h1>
<p class="abs hero-sub">A powerful CX platform combined with<br>expert consulting services</p>
<a class="abs btn btn-primary" style="left:144px;top:565px;width:202px;height:51px">Request a Demo
  <svg width="20" height="20" viewBox="0 0 20 20"><path d="M10 1l4 4-4 4-4-4zM10 11l4 4-4 4-4-4z" fill="none" stroke="#fff" stroke-width="2"/></svg></a>
<a class="abs btn btn-outline" style="left:357px;top:565px;width:172px;height:51px">Learn More
  <svg width="20" height="20" viewBox="0 0 20 20"><path d="M10 1l4 4-4 4-4-4z" fill="none" stroke="var(--blue)" stroke-width="2"/><path d="M10 11l4 4-4 4-4-4z" fill="none" stroke="var(--orange)" stroke-width="2"/></svg></a>

<!-- hero dashboard -->
<svg class="abs" style="left:584px;top:291px;filter:drop-shadow(0 8px 18px rgba(40,60,120,.15))" width="474" height="326" viewBox="0 0 474 326">
  <rect width="474" height="326" rx="20" fill="#e6eafb"/>
  <rect x="18" y="18" width="438" height="288" rx="8" fill="#fff"/>
  <rect x="18" y="18" width="84" height="288" fill="#f7f8fc"/>
  <circle cx="60" cy="52" r="11" fill="#dfe6f8"/><circle cx="60" cy="50" r="4" fill="var(--blue)"/>
  <g font-family="Roboto,sans-serif" font-size="7" fill="#8a8d98">
    <text x="54" y="84">Home</text>
    <rect x="32" y="92" width="60" height="11" rx="3" fill="var(--blue)"/><text x="54" y="100" fill="#fff">Dashboard</text>
    <text x="54" y="130">Admin</text><text x="54" y="152">Messages</text><text x="54" y="174">Settings</text>
    <text x="44" y="282">Logout</text>
    <text x="112" y="34" fill="#333" font-size="8">Dashboard</text>
    <text x="112" y="134">Activity</text><text x="302" y="134">Overview</text>
  </g>
  <g fill="var(--blue)">
    <rect x="124" y="78" width="3" height="18"/><rect x="130" y="70" width="3" height="26"/><rect x="136" y="84" width="3" height="12"/>
    <rect x="142" y="74" width="3" height="22"/><rect x="148" y="80" width="3" height="16"/><rect x="154" y="66" width="3" height="30"/>
    <rect x="160" y="84" width="3" height="12"/><rect x="166" y="72" width="3" height="24"/><rect x="172" y="62" width="3" height="34"/>
    <rect x="178" y="78" width="3" height="18"/><rect x="184" y="70" width="3" height="26"/><rect x="190" y="82" width="3" height="14"/>
    <rect x="196" y="68" width="3" height="28"/><rect x="202" y="76" width="3" height="20"/><rect x="208" y="58" width="3" height="38"/>
    <rect x="214" y="72" width="3" height="24"/><rect x="220" y="80" width="3" height="16"/><rect x="226" y="66" width="3" height="30"/>
    <rect x="232" y="56" width="3" height="40"/><rect x="238" y="74" width="3" height="22"/><rect x="244" y="64" width="3" height="32"/>
    <rect x="250" y="52" width="3" height="44"/><rect x="256" y="70" width="3" height="26"/><rect x="262" y="60" width="3" height="36"/>
    <rect x="268" y="50" width="3" height="46"/><rect x="274" y="72" width="3" height="24"/>
  </g>
  <rect x="296" y="38" width="50" height="70" fill="#f4f6fb"/>
  <rect x="300" y="90" width="8" height="8" fill="var(--blue)"/><rect x="312" y="90" width="8" height="8" fill="var(--blue)"/><rect x="324" y="90" width="8" height="8" fill="var(--blue)"/>
  <rect x="356" y="40" width="84" height="24" rx="3" fill="var(--blue)"/><rect x="356" y="70" width="84" height="24" rx="3" fill="var(--blue)"/>
  <polyline points="112,190 130,160 150,176 170,170 190,184 210,168 230,174 250,150 270,186 290,170" fill="none" stroke="var(--orange)" stroke-width="1.5"/>
  <polyline points="112,170 130,178 150,162 170,180 190,166 210,176 230,182 250,170 270,162 290,176" fill="none" stroke="var(--blue)" stroke-width="1.5"/>
  <g fill="none" stroke-width="4">
    <circle cx="316" cy="156" r="9" stroke="var(--blue)"/><circle cx="362" cy="156" r="9" stroke="#e9edf5"/><circle cx="362" cy="156" r="9" stroke="var(--orange)" stroke-dasharray="30 60"/>
    <circle cx="316" cy="184" r="9" stroke="var(--orange)"/><circle cx="362" cy="184" r="9" stroke="#2bb673"/>
  </g>
  <rect x="110" y="212" width="180" height="80" fill="#fafbfd"/>
  <g fill="var(--blue)"><rect x="130" y="258" width="4" height="26"/><rect x="140" y="266" width="4" height="18"/><rect x="150" y="250" width="4" height="34"/><rect x="170" y="262" width="4" height="22"/><rect x="180" y="254" width="4" height="30"/><rect x="200" y="260" width="4" height="24"/><rect x="220" y="248" width="4" height="36"/><rect x="240" y="264" width="4" height="20"/><rect x="260" y="252" width="4" height="32"/></g>
  <g fill="var(--orange)"><rect x="160" y="270" width="4" height="14"/><rect x="210" y="266" width="4" height="18"/><rect x="250" y="270" width="4" height="14"/></g>
  <circle cx="338" cy="254" r="26" fill="none" stroke="var(--blue)" stroke-width="6"/>
  <circle cx="338" cy="254" r="26" fill="none" stroke="var(--orange)" stroke-width="6" stroke-dasharray="60 200"/>
  <text x="338" y="257" text-anchor="middle" font-family="Roboto,sans-serif" font-size="8" font-weight="700" fill="#333">21,424</text>
  <circle cx="414" cy="254" r="24" fill="none" stroke="#f2c14e" stroke-width="8"/>
  <circle cx="414" cy="254" r="24" fill="none" stroke="#2bb673" stroke-width="8" stroke-dasharray="50 200"/>
  <circle cx="414" cy="254" r="24" fill="none" stroke="var(--orange)" stroke-width="8" stroke-dasharray="30 200" stroke-dashoffset="-60"/>
  <text x="414" y="257" text-anchor="middle" font-family="Roboto,sans-serif" font-size="8" font-weight="700" fill="#333">940</text>
</svg>

<div class="abs dots"><i></i><i></i><i class="on"></i><i></i></div>

<!-- what we offer -->
<svg class="abs" style="left:0;top:830px" width="1200" height="810" viewBox="0 0 1200 810">
  <defs>
    <linearGradient id="offerBg" x1="0" y1="0" x2="0" y2="1"><stop offset="0" stop-color="#fff"/><stop offset=".35" stop-color="var(--bg-soft)"/><stop offset="1" stop-color="#f5f6f9"/></linearGradient>
    <linearGradient id="featureGrad" x1="0" y1="0" x2="0" y2="1"><stop offset="0" stop-color="var(--orange)"/><stop offset="1" stop-color="var(--blue)"/></linearGradient>
    <filter id="sh" x="-20%" y="-20%" width="140%" height="140%"><feDropShadow dx="0" dy="6" stdDeviation="10" flood-color="#2a3050" flood-opacity=".14"/></filter>
  </defs>
  <rect width="1200" height="810" fill="url(#offerBg)"/>
  <polygon points="0,330 600,780 1200,330 1200,560 600,810 0,560" fill="#e9ebf0" opacity=".6"/>
  <polyline points="86,364 56,394 86,424" fill="none" stroke="#9aa0ab" stroke-width="1.5"/>
  <polyline points="1114,364 1144,394 1114,424" fill="none" stroke="#9aa0ab" stroke-width="1.5"/>
  <!-- left card -->
  <rect x="295" y="214" width="60" height="5" rx="2" fill="var(--orange)"/>
  <polygon points="325,234 501,394 325,552 149,394" fill="#fff" filter="url(#sh)"/>
  <rect x="295" y="570" width="60" height="5" rx="2" fill="var(--blue)"/>
  <!-- right card -->
  <rect x="845" y="214" width="60" height="5" rx="2" fill="var(--orange)"/>
  <polygon points="875,234 1051,394 875,552 699,394" fill="#fff" filter="url(#sh)"/>
  <rect x="845" y="570" width="60" height="5" rx="2" fill="var(--blue)"/>
  <!-- feature card -->
  <rect x="566" y="280" width="70" height="6" rx="3" fill="var(--orange)"/>
  <polygon points="601,304 795,505 601,698 407,505" fill="url(#featureGrad)" filter="url(#sh)"/>
  <rect x="566" y="716" width="70" height="6" rx="3" fill="var(--blue)"/>
  <!-- icons -->
  <g fill="none" stroke="var(--blue)" stroke-width="2.5" transform="translate(295,280)">
    <rect x="2" y="2" width="54" height="20" rx="3"/>
    <path d="M12 7l2 4 4 .5-3 3 .8 4-3.8-2-3.8 2 .8-4-3-3 4-.5zM29 7l2 4 4 .5-3 3 .8 4-3.8-2-3.8 2 .8-4-3-3 4-.5zM46 7l2 4 4 .5-3 3 .8 4-3.8-2-3.8 2 .8-4-3-3 4-.5z" stroke-width="1.5"/>
    <rect x="2" y="28" width="54" height="24" rx="3"/><path d="M9 36h28M9 44h20M40 54l16-16"/>
  </g>
  <g fill="none" stroke="var(--blue)" stroke-width="2.5" transform="translate(847,278)">
    <circle cx="28" cy="22" r="18"/>
    <path d="M28 12l3 7 7 .6-5.3 4.6 1.7 7-6.4-3.8-6.4 3.8 1.7-7L18 19.6l7-.6z" stroke-width="2"/>
    <path d="M6 36c2 12 10 20 22 22M50 36c-2 12-10 20-22 22"/>
  </g>
  <g fill="none" stroke="#fff" stroke-width="2.5" transform="translate(566,387)">
    <rect x="2" y="2" width="60" height="46" rx="3"/><path d="M2 10h60"/>
    <path d="M12 40V28M20 40V20M28 40V30"/><circle cx="46" cy="34" r="10"/><path d="M53 41l10 10"/>
    <path d="M41 36l4-5 3 3 4-5" stroke-width="1.8"/>
  </g>
  <g fill="none" stroke="var(--orange)" stroke-width="2">
    <circle cx="325" cy="508" r="13"/><polyline points="319,505 325,511 331,505"/>
    <circle cx="875" cy="508" r="13"/><polyline points="869,505 875,511 881,505"/>
  </g>
  <g fill="none" stroke="#fff" stroke-width="2"><circle cx="601" cy="639" r="16"/><polyline points="594,636 601,643 608,636"/></g>
</svg>

<h2 class="abs sec-title" style="top:933px"><strong>WHAT</strong> WE OFFER</h2>

<div class="abs offer-text" style="left:205px;top:1188px"><h3>COLLECT FEEDBACK</h3><p>Sed ut perspiciatis unde omnis iste natus error sit voluptatem accusror sit volantium</p></div>
<div class="abs offer-text" style="left:755px;top:1188px"><h3>IMPROVE LOYALTY</h3><p>Sed ut perspiciatis unde omnis iste natus error sit voluptatem accusror sit volantium</p></div>
<div class="abs offer-text feature" style="left:466px;top:1305px"><h3>ANALYZE INSIGHTS</h3><p>Sed ut perspiciatis unde omnis iste natus error sit voluptatem accusror sit volantium</p></div>

<!-- who we are -->
<svg class="abs" style="left:0;top:1641px" width="1200" height="608" viewBox="0 0 1200 608">
  <defs><linearGradient id="blueBg" x1="0" y1="0" x2="1" y2="1"><stop offset="0" stop-color="var(--blue)"/><stop offset="1" stop-color="var(--blue-dark)"/></linearGradient></defs>
  <polygon points="382,0 1200,0 1200,608 430,608 330,480 330,120" fill="url(#blueBg)"/>
</svg>
<div class="abs accent-who" role="img" aria-label="Decorative orange and blue geometric accent"></div>

<svg class="abs" style="left:143px;top:1769px;filter:drop-shadow(0 8px 10px rgba(13,27,64,.25))" width="422" height="290" viewBox="0 0 422 290">
  <rect width="422" height="290" rx="16" fill="#fff"/>
  <g font-family="Roboto,sans-serif" font-size="6" fill="#9aa0ab">
    <rect x="32" y="16" width="358" height="258" fill="#f7f8fb"/>
    <circle cx="40" cy="24" r="2" fill="#ccc"/><circle cx="47" cy="24" r="2" fill="#ccc"/><circle cx="54" cy="24" r="2" fill="#ccc"/>
    <rect x="40" y="34" width="342" height="110" fill="#fff"/>
    <text x="48" y="46">Satisfaction trend</text><text x="330" y="46">Last 12 mo</text>
    <path d="M60 116 C90 100 110 90 130 98 S170 112 190 100 S230 80 250 96 S290 116 310 104 S350 92 370 100" fill="none" stroke="#5b6ee8" stroke-width="2"/>
    <path d="M52 128h320" stroke="#eee"/>
    <rect x="40" y="152" width="220" height="114" fill="#fff"/><text x="48" y="164">Responses</text>
    <g fill="#5b6ee8"><rect x="60" y="210" width="5" height="36"/><rect x="72" y="200" width="5" height="46"/><rect x="84" y="216" width="5" height="30"/><rect x="96" y="206" width="5" height="40"/><rect x="108" y="224" width="5" height="22"/><rect x="120" y="230" width="5" height="16"/><rect x="132" y="212" width="5" height="34"/><rect x="144" y="222" width="5" height="24"/><rect x="156" y="204" width="5" height="42"/><rect x="168" y="218" width="5" height="28"/><rect x="180" y="198" width="5" height="48"/><rect x="192" y="208" width="5" height="38"/><rect x="204" y="226" width="5" height="20"/><rect x="216" y="232" width="5" height="14"/></g>
    <rect x="268" y="152" width="114" height="114" fill="#fff"/><text x="276" y="164">NPS score</text>
    <circle cx="325" cy="214" r="24" fill="none" stroke="#5b6ee8" stroke-width="8"/>
    <circle cx="325" cy="214" r="24" fill="none" stroke="#8fe3d2" stroke-width="8" stroke-dasharray="40 200"/>
    <rect x="48" y="254" width="200" height="3" fill="#e8eaf2"/><rect x="276" y="254" width="96" height="3" fill="#e8eaf2"/>
  </g>
</svg>

<h2 class="abs who-title"><strong>WHO</strong> WE ARE</h2>
<p class="abs who-copy">Sed ut perspiciatis unde omnis iste natus error sit voluptatem accusantium doloremque laudantium, totam rem aperiam, eaque ipsa quae ab illo inventore veritatis et quasi architecto beatae vitae dicta sunt explicabo. Nemo enim ipsam voluptatem quia voluptas sit aspernatur aut odit aut fugit, sed quia consequuntur magni dolores eos qui ratione voluptatem sequi nesciunt. Neque porro quisquam est, qui dolorem ipsum quia dolor sit amet</p>
<a class="abs btn btn-primary" style="left:623px;top:2081px;width:179px;height:50px">Learn More
  <svg width="20" height="20" viewBox="0 0 20 20"><path d="M10 1l4 4-4 4-4-4zM10 11l4 4-4 4-4-4z" fill="none" stroke="#fff" stroke-width="2"/></svg></a>

<!-- case studies -->
<h2 class="abs sec-title" style="top:2360px"><strong>CASE</strong> STUDIES</h2>
<svg class="abs" style="left:0;top:2530px" width="1200" height="80" viewBox="0 0 1200 80">
  <polyline points="86,10 56,40 86,70" fill="none" stroke="#9aa0ab" stroke-width="1.5"/>
  <polyline points="1114,10 1144,40 1114,70" fill="none" stroke="#9aa0ab" stroke-width="1.5"/>
</svg>

<article class="abs case" style="left:156px;top:2477px;width:277px;height:186px">
  <div class="case-head"><div class="date" style="background:var(--blue)"><b>02</b><span>JAN</span></div><h4>Pellentesque faucibus Ut accumsan ultric</h4></div>
  <p>Duis quam Nam eget lacus Aliquam erat volutpat Quisque dignissim congue leovel lacus vitae felis</p><a class="more">READ MORE</a>
</article>
<article class="abs case lift" style="left:462px;top:2477px;width:277px;height:186px">
  <div class="case-head"><div class="date" style="background:var(--orange)"><b>02</b><span>JAN</span></div><h4>Pellentesque faucibus Ut accumsan ultric</h4></div>
  <p>Duis quam Nam eget lacus Aliquam erat volutpat Quisque dignissim congue leovel lacus vitae felis</p><a class="more">READ MORE</a>
</article>
<article class="abs case" style="left:767px;top:2477px;width:277px;height:186px">
  <div class="case-head"><div class="date" style="background:var(--blue)"><b>02</b><span>JAN</span></div><h4>Pellentesque faucibus Ut accumsan ultric</h4></div>
  <p>Duis quam Nam eget lacus Aliquam erat volutpat Quisque dignissim congue leovel lacus vitae felis</p><a class="more">READ MORE</a>
</article>

<a class="abs btn btn-primary" style="left:511px;top:2709px;width:179px;height:51px">View More
  <svg width="20" height="20" viewBox="0 0 20 20"><path d="M10 1l4 4-4 4-4-4zM10 11l4 4-4 4-4-4z" fill="none" stroke="#fff" stroke-width="2"/></svg></a>

<!-- reviews -->
<svg class="abs" style="left:0;top:2851px" width="1200" height="408" viewBox="0 0 1200 408">
  <defs><linearGradient id="revGrad" x1="0" y1="0" x2="1" y2="0"><stop offset="0" stop-color="var(--orange)"/><stop offset="1" stop-color="var(--orange-dark)"/></linearGradient></defs>
  <polygon points="0,0 1000,0 1183,203 1000,408 0,408" fill="url(#revGrad)"/>
  <polyline points="144,170 112,203 144,236" fill="none" stroke="#fff" stroke-width="1.5" opacity=".8"/>
  <polyline points="1056,170 1088,203 1056,236" fill="none" stroke="#fff" stroke-width="1.5" opacity=".8"/>
</svg>
<h2 class="abs rev-title"><strong>CUSTOMER</strong> REVIEWS</h2>
<p class="abs rev-quote">"At vero eos et accusamus et iusto odio dignissimos ducimus qui blanditiis praesentium voluptatum deleniti atque corrupti quos dolores et quas molestias excepturi sint occaecati cupiditate non provident, similique sunt in culpa qui officia deseruaborum et dolorum fuga."</p>
<div class="abs rev-name">-MARA LINDQVIST , Customer
  <svg width="110" height="20" viewBox="0 0 110 20" fill="#fff">
    <g id="st"><path d="M10 1l2.6 6 6.4.6-4.9 4.3 1.5 6.3L10 15l-5.6 3.2 1.5-6.3L1 7.6 7.4 7z"/></g>
    <use href="#st" x="22"/><use href="#st" x="44"/><use href="#st" x="66"/><use href="#st" x="88"/>
  </svg>
</div>

<!-- footer -->
<div class="abs f-brand"><span class="brand-mark" style="width:30px;height:30px"></span><span class="brand-name" style="font-size:34px">PollMeridian</span></div>

<div class="abs f-contact" style="left:252px;top:3478px">
  <div class="diamond-ico" style="background:var(--blue);width:30px;height:30px"><svg width="12" height="12" viewBox="0 0 24 24"><path fill="#fff" d="M12 2a7 7 0 0 0-7 7c0 5 7 13 7 13s7-8 7-13a7 7 0 0 0-7-7zm0 9.5A2.5 2.5 0 1 1 12 6.5a2.5 2.5 0 0 1 0 5z"/></svg></div>
  <span>123, At vero eos et accusamus<br>et iusto odio dignissimos</span>
</div>
<div class="abs f-contact" style="left:528px;top:3488px">
  <div class="diamond-ico" style="background:var(--orange);width:30px;height:30px"><svg width="12" height="12" viewBox="0 0 24 24"><path fill="#fff" d="M6.6 10.8c1.4 2.8 3.8 5.2 6.6 6.6l2.2-2.2c.3-.3.7-.4 1-.2 1.1.4 2.3.6 3.6.6.6 0 1 .4 1 1V20c0 .6-.4 1-1 1C10.6 21 3 13.4 3 4c0-.6.4-1 1-1h3.5c.6 0 1 .4 1 1 0 1.3.2 2.5.6 3.6.1.3 0 .7-.2 1z"/></svg></div>
  <span style="font-size:16px;font-weight:500;color:var(--navy)">+1 555 014 2090</span>
</div>
<div class="abs f-contact" style="left:740px;top:3488px">
  <div class="diamond-ico" style="background:var(--blue);width:30px;height:30px"><svg width="12" height="12" viewBox="0 0 24 24"><path fill="#fff" d="M2 5h20v14H2zm2 2v.5l8 5 8-5V7l-8 5z"/></svg></div>
  <span>hello@pollmeridian.io</span>
</div>

<nav class="abs f-nav"><a>HOME</a><a>PRODUCTS</a><a>ABOUT</a><a>BLOG</a><a>CONTACT</a><a>PRICING</a></nav>
<p class="abs copy">Copyright 2025 PollMeridian. All Rights Reserved &nbsp;|&nbsp; Privacy Policy &nbsp;|&nbsp; Terms of Use</p>
<div class="abs social" aria-label="Social links"><i style="background:var(--blue)"></i><i style="background:var(--orange)"></i><i style="background:var(--navy)"></i></div>

</body>
</html>
```